Book cover design for Water & Sanitation book

I would like to have a book cover designed (front and back) for a book I'm writing that has interviews with leading experts working in the field of water & sanitation globally.

Please use this board - https://in.moodtrellis.com/kovanshelarji/pins/ - as inspiration.

The title of the book is "Lanterns Over Marble" and will need to be visible on the cover page. The size of the book will be portrait and 8 inches x 11 inches.

```html
<!DOCTYPE html>
<html lang="en">
<head>
<meta charset="utf-8">
<title>Lanterns Over Marble — Book Cover</title>
<link href="https://fonts.googleapis.com/css2?family=Libre+Baskerville:ital,wght@0,400;0,700;1,700&display=swap" rel="stylesheet">
<style>
  :root {
    --backdrop: #e3e7ea;
    --water-light: #7cc3c9;
    --water-mid: #4d9fb3;
    --water-deep: #22628d;
    --water-dark: #153f66;
    --band: #f7f8f8;
    --ink: #1f3550;
  }
  * { margin: 0; padding: 0; box-sizing: border-box; }
  html, body {
    width: 1200px;
    height: 720px;
    overflow: hidden;
    background: var(--backdrop);
  }
  .stage {
    position: relative;
    width: 1200px;
    height: 720px;
  }
  .book-cover {
    position: absolute;
    left: 367px;
    top: 40px;
    width: 466px;
    height: 640px;
    overflow: hidden;
  }
  .cover-photo {
    position: absolute;
    inset: 0;
    background:
      radial-gradient(ellipse 62% 38% at 60% 58%, var(--water-dark) 0%, var(--water-deep) 28%, var(--water-mid) 58%, transparent 100%),
      linear-gradient(160deg, var(--water-light) 0%, var(--water-mid) 55%, var(--water-deep) 100%);
  }
  .title-band {
    position: absolute;
    left: 0;
    right: 0;
    top: 50px;
    height: 92px;
    background: var(--band);
    display: flex;
    flex-direction: column;
    align-items: center;
    justify-content: center;
    gap: 8px;
  }
  .book-title {
    font-family: "Libre Baskerville", Georgia, serif;
    font-weight: 700;
    font-size: 25px;
    letter-spacing: 0.12em;
    text-transform: uppercase;
    color: var(--ink);
    white-space: nowrap;
  }
  .book-author {
    font-family: "Libre Baskerville", Georgia, serif;
    font-weight: 700;
    font-style: italic;
    font-size: 15px;
    letter-spacing: 0.06em;
    color: var(--ink);
  }
</style>
</head>
<body>
  <main class="stage">
    <section class="book-cover">
      <div class="cover-photo" role="img" aria-label="Photograph of a water droplet falling into still blue water, with concentric ripples spreading out"></div>
      <header class="title-band">
        <h1 class="book-title">Lanterns Over Marble</h1>
        <p class="book-author">Author</p>
      </header>
    </section>
  </main>
</body>
</html>
```